1887 Basins & Spouts Business Card

I'm wanting to get a business card designed. Our business is 1887 Basins & Spouts
Details for the card:

1887 Basins & Spouts
Name: Warren Tobbit
Email: warren@1887basinsandspouts.com.au
Website: www.1887basinsandspouts.com.au
Mobile: 0438 169 204
Phone: 02 6187 4932

Font of Basins & Spouts is called Snell Roundhand. Not sue what font logo text is.

I'm thinking two sided but it doesn't have to be.

```html
<!DOCTYPE html>
<html lang="en">
<head>
<meta charset="utf-8">
<title>1887 Basins &amp; Spouts – Business Card</title>
<link rel="stylesheet" href="https://fonts.googleapis.com/css2?family=Pinyon+Script&family=Josefin+Sans:wght@300&family=Open+Sans:wght@600&display=swap">
<style>
  :root {
    --backdrop: #ececee;
    --front-pink: #fce5e3;
    --back-white: #ffffff;
    --ink: #141414;
    --gold: #a8875c;
    --name-brown: #85654a;
    --contact-pink: #d59aa1;
  }
  * { margin: 0; padding: 0; box-sizing: border-box; }
  html, body {
    width: 1200px;
    height: 895px;
    overflow: hidden;
    background: var(--backdrop);
  }
  .canvas {
    position: relative;
    width: 1200px;
    height: 895px;
  }
  .card {
    position: absolute;
    width: 480px;
    height: 280px;
    box-shadow: 0 6px 18px rgba(0, 0, 0, 0.10);
  }

  /* Front side */
  .card-front {
    left: 250px;
    top: 190px;
    background: var(--front-pink);
  }
  .brand-lockup {
    position: absolute;
    left: 46px;
    top: 104px;
    display: flex;
    align-items: center;
    gap: 16px;
  }
  .brand-mark {
    flex: none;
    width: 62px;
    height: 62px;
    border: 3px solid var(--ink);
    border-radius: 50%;
  }
  .brand-text {
    display: flex;
    flex-direction: column;
    align-items: flex-end;
  }
  .brand-name {
    font-family: "Pinyon Script", cursive;
    font-weight: 400;
    font-size: 34px;
    line-height: 1.1;
    color: var(--ink);
    white-space: nowrap;
  }
  .tagline {
    margin-top: 4px;
    font-family: "Open Sans", sans-serif;
    font-weight: 600;
    font-size: 10.5px;
    color: var(--ink);
    white-space: nowrap;
  }

  /* Back side */
  .card-back {
    left: 500px;
    top: 505px;
    background: var(--back-white);
  }
  .frame {
    position: absolute;
    inset: 0;
  }
  .holder-name {
    position: absolute;
    top: 60px;
    width: 100%;
    text-align: center;
    font-family: "Pinyon Script", cursive;
    font-weight: 400;
    font-size: 36px;
    line-height: 1;
    color: var(--name-brown);
  }
  .contact-list {
    position: absolute;
    left: 0;
    top: 130px;
    width: 100%;
    display: grid;
    grid-template-columns: 162px auto;
    column-gap: 10px;
    row-gap: 3px;
    font-family: "Josefin Sans", sans-serif;
    font-weight: 300;
    font-size: 14px;
    color: var(--contact-pink);
  }
  .contact-label { text-align: right; }
  .contact-value { white-space: nowrap; }
</style>
</head>
<body>
  <main class="canvas">
    <section class="card card-front" aria-label="Business card front">
      <div class="brand-lockup">
        <span class="brand-mark" aria-hidden="true"></span>
        <div class="brand-text">
          <h1 class="brand-name">1887 Basins &amp; Spouts</h1>
          <p class="tagline">Classic elegance meets everyday reliability, always</p>
        </div>
      </div>
    </section>

    <section class="card card-back" aria-label="Business card back">
      <svg class="frame" width="480" height="280" viewBox="0 0 480 280" aria-hidden="true">
        <rect x="26" y="36" width="428" height="208" fill="none" stroke="var(--gold)" stroke-width="1.2"/>
        <rect x="32" y="42" width="416" height="196" fill="none" stroke="var(--gold)" stroke-width="1.2"/>
      </svg>
      <h2 class="holder-name">Warren Tobbit</h2>
      <dl class="contact-list">
        <dt class="contact-label">Email:</dt>
        <dd class="contact-value">warren@1887basinsandspouts.com.au</dd>
        <dt class="contact-label">Website:</dt>
        <dd class="contact-value">www.1887basinsandspouts.com.au</dd>
        <dt class="contact-label">Mobile:</dt>
        <dd class="contact-value">0438 169 204</dd>
        <dt class="contact-label">Phone:</dt>
        <dd class="contact-value">02 6187 4932</dd>
      </dl>
    </section>
  </main>
</body>
</html>
```